BLUE FORGE (Business Card for Training Company)

Blue Forge is a training and consultancy company with a focus on executive protection and medical. I would like the card to be nice and sharp, not overdone and in black and red. I would also like it to highlight that it is "A Tavmont Company"

I would like it to be simple and highlight a few things.

1. Name
2. Title
3. Phone Number
4. Email

I would also like www.tavmontgroup.example/blue-forge to be on the card somewhere.

Target Market(s)

Security Companies

Industry/Entity Type

Security

Contact Information for Business Card

Blue Forge is a training and consultancy company with a focus on executive protection and medical. I would like the card to be nice and sharp, not overdone and in black and red. I would also like it to highlight that it is "A Tavmont Company" I would like it to be simple and highlight a few things. 1. Name 2. Title 3. Phone Number 4. Email I would also like www.tavmontgroup.example/blue-forge to be on the card somewhere.

Requirements
Must have
• A Tavmont Company listed on the card and the website
Nice to have
• Highlight Medical Training, Consultancy & Executive Protection Courses

```html
<!DOCTYPE html>
<html lang="en">
<head>
<meta charset="utf-8">
<title>Blue Forge Business Card</title>
<link rel="stylesheet" href="https://fonts.googleapis.com/css2?family=Open+Sans:wght@400;600;700;800&display=swap">
<style>
  :root {
    --stage: #3d3d3d;
    --paper: #ffffff;
    --brand-red: #6b0f12;
    --deep-red: #5c0b0e;
    --mark-red: #7a1a1d;
    --ink: #1a1a1a;
    --muted: #6a6a6a;
  }
  html, body {
    margin: 0;
    width: 1200px;
    height: 801px;
    overflow: hidden;
    background: var(--stage);
    font-family: "Open Sans", Arial, sans-serif;
  }
  .card {
    position: absolute;
    width: 540px;
    height: 309px;
    box-sizing: border-box;
    box-shadow: 0 10px 30px rgba(0,0,0,0.35);
  }
  .card-front {
    left: 40px;
    top: 90px;
    background: var(--paper);
    border-bottom: 3px solid var(--brand-red);
  }
  .front-wordmark {
    position: absolute;
    left: 36px;
    top: 92px;
    width: 200px;
    color: var(--brand-red);
    font-weight: 800;
    font-size: 50px;
    line-height: 0.95;
    letter-spacing: 1px;
  }
  .divider {
    position: absolute;
    left: 252px;
    top: 70px;
    width: 1px;
    height: 128px;
    background: var(--brand-red);
  }
  .contact {
    position: absolute;
    left: 272px;
    top: 70px;
  }
  .person-name {
    margin: 0;
    color: var(--brand-red);
    font-weight: 800;
    font-size: 20px;
    letter-spacing: 0.3px;
  }
  .person-title {
    margin: 0 0 14px;
    color: var(--muted);
    font-size: 14px;
  }
  .contact-list {
    list-style: none;
    margin: 0;
    padding: 0 0 0 20px;
  }
  .contact-list li {
    display: flex;
    align-items: center;
    gap: 7px;
    color: var(--muted);
    font-size: 12.5px;
    line-height: 21px;
  }
  .contact-list svg { width: 11px; height: 11px; fill: var(--brand-red); flex: none; }
  .services {
    position: absolute;
    left: 0;
    right: 0;
    bottom: 26px;
    text-align: center;
    color: var(--muted);
    font-size: 13px;
    letter-spacing: 0.3px;
  }
  .services .dot { color: var(--brand-red); margin: 0 8px; }

  .card-back {
    left: 620px;
    top: 400px;
    background: var(--deep-red);
    overflow: hidden;
  }
  .back-wordmark {
    position: absolute;
    left: 0;
    right: 0;
    top: 70px;
    text-align: center;
    color: var(--mark-red);
    font-weight: 800;
    font-size: 58px;
    line-height: 0.95;
    letter-spacing: 1px;
  }
  .parent-tab {
    position: absolute;
    left: 50%;
    bottom: 0;
    transform: translateX(-50%);
    width: 330px;
    height: 44px;
  }
  .parent-tab svg { position: absolute; inset: 0; width: 100%; height: 100%; }
  .parent-tab span {
    position: relative;
    display: block;
    text-align: center;
    line-height: 46px;
    color: var(--ink);
    font-weight: 700;
    font-size: 19px;
    letter-spacing: 0.8px;
  }
</style>
</head>
<body>

<section class="card card-front">
  <div class="front-wordmark">BLUE<br>FORGE</div>
  <div class="divider"></div>
  <div class="contact">
    <p class="person-name">DAREN HOLTWICK</p>
    <p class="person-title">President</p>
    <ul class="contact-list">
      <li><svg viewBox="0 0 16 16"><path d="M3 1l3 3-2 2c1 2 3 4 6 6l2-2 3 3-2 3C7 15 1 9 1 3z"/></svg>555-014-2290</li>
      <li><svg viewBox="0 0 16 16"><path d="M1 3h14v10H1z M1 3l7 6 7-6" fill="none" stroke="#6b0f12" stroke-width="2"/></svg>info@tavmontgroup.example</li>
      <li><svg viewBox="0 0 16 16"><circle cx="8" cy="8" r="7"/></svg>www.tavmontgroup.example/blue-forge</li>
    </ul>
  </div>
  <div class="services">Medical Training<span class="dot">•</span>Consultancy<span class="dot">•</span>Executive Protection Courses</div>
</section>

<section class="card card-back">
  <div class="back-wordmark">BLUE<br>FORGE</div>
  <div class="parent-tab">
    <svg viewBox="0 0 330 44" preserveAspectRatio="none"><polygon points="18,0 312,0 330,44 0,44" fill="#ffffff"/></svg>
    <span>A TAVMONT COMPANY</span>
  </div>
</section>

</body>
</html>
```